A modern, fresh introduction to Buddhism

I need a book cover for an A6 sized book to be used both for ebook and hard copy. The author is a young, modern Buddhist teacher of high standing who has written this short intro to Buddhism in an informal Q & As format using modern, accessible language to convey profound and meaningful ideas to the general public. The author is Tibetan, but teaches worldwide and is very personable and dynamic. The cover should portray this and have a fresh yet authentic feel to it (nothing new-agey!). Please see the author's websites www.norvalemtasheteacher.org and www.pwrt.org for reference, but do not feel that the design must align completely with the website designs.

Target Market(s)

General public both in Europe and America and in Asia ranging from teenagers to the elderly. A really broad audience.

Industry/Entity Type

Teacher

Requirements
Must have
• Please include the following text that on the front cover:

A Window onto Stillness

By Drawa Tsomen Lhundrup

Please include the following on the back cover:

Yunor Trenpa Publications (with attached logo above it)
Nice to have
• A simplistic, artistic, and modern look without any traditional religious images.
Should not have
• No buddha images or religious images. I would prefer a more simplistic, modern and artistic look.

```html
<!DOCTYPE html>
<html lang="en">
<head>
<meta charset="utf-8">
<title>A Window onto Stillness — Book Cover</title>
<link href="https://fonts.googleapis.com/css2?family=EB+Garamond:wght@400;500&family=Vollkorn:wght@700&display=swap" rel="stylesheet">
<style>
  :root {
    --cover-violet: #6f52a2;
    --photo-deep: #7650a6;
    --photo-glow: #c08cc4;
    --photo-mid: #9868b3;
    --text-white: #ffffff;
    --subtitle-pink: #d6a8d4;
  }
  html, body {
    margin: 0;
    padding: 0;
    overflow: hidden;
    background: var(--cover-violet);
  }
  .cover {
    position: relative;
    width: 848px;
    height: 1200px;
    background: var(--cover-violet);
    overflow: hidden;
  }
  .cover__image {
    position: absolute;
    top: 0;
    left: 0;
    width: 848px;
    height: 571px;
    background:
      radial-gradient(ellipse 60% 55% at 52% 100%, var(--photo-glow) 0%, rgba(192,140,196,0) 100%),
      radial-gradient(ellipse 45% 40% at 85% 10%, rgba(170,130,200,0.6) 0%, rgba(170,130,200,0) 100%),
      linear-gradient(180deg, var(--photo-deep) 0%, var(--photo-mid) 100%);
  }
  .cover__author {
    position: absolute;
    top: 78px;
    left: 0;
    width: 100%;
    text-align: center;
    font-family: "EB Garamond", Georgia, serif;
    font-weight: 400;
    font-size: 27px;
    color: var(--text-white);
    margin: 0;
    letter-spacing: 0.3px;
  }
  .cover__title {
    position: absolute;
    top: 716px;
    left: 0;
    width: 100%;
    margin: 0;
    text-align: center;
    font-family: "Vollkorn", Georgia, serif;
    font-weight: 700;
    font-size: 78px;
    line-height: 104px;
    letter-spacing: 1px;
    color: var(--text-white);
    text-transform: uppercase;
  }
  .cover__subtitle {
    position: absolute;
    top: 950px;
    left: 0;
    width: 100%;
    margin: 0;
    text-align: center;
    font-family: "EB Garamond", Georgia, serif;
    font-weight: 400;
    font-size: 35px;
    color: var(--subtitle-pink);
  }
</style>
</head>
<body>
  <main class="cover">
    <div class="cover__image" role="img" aria-label="Soft-focus photograph of glowing bokeh light circles on a violet background"></div>
    <p class="cover__author">Drawa Tsomen Lhundrup</p>
    <h1 class="cover__title">A Window onto<br>Stillness</h1>
    <p class="cover__subtitle">A Short Introduction to the Buddha's Teaching</p>
  </main>
</body>
</html>
```